Ironvale Shift Services

We are a underground coal mining labour hire company, needing a website that links into our online payroll (www.wagetrakker.com.au) and also need to have job applications page that is a preform with drop down menu,s with answers or check boxes. We would also need a 3 tier administration access for access to different files.
We are looking for an ongoing relationship with future app integration

Reason: There are a few more designs to come and I'm out at the mine for another week

Industry/Entity Type

Coal Mining

```html
<!DOCTYPE html>
<html lang="en">
<head>
<meta charset="utf-8">
<title>Ironvale Shift Services – Application Form</title>
<link href="https://fonts.googleapis.com/css2?family=Arimo:wght@400;700&family=Orbitron:wght@500&display=swap" rel="stylesheet">
<style>
  :root {
    --bg: #000000;
    --panel: #1a1a1a;
    --panel-alt: #000000;
    --rule: #4a4a4a;
    --orange: #ff8a2b;
    --text: #8e8e8e;
    --text-strong: #b5b5b5;
    --white: #ffffff;
    --muted: #555555;
  }
  * { margin: 0; padding: 0; box-sizing: border-box; }
  html, body { width: 1200px; height: 1042px; overflow: hidden; background: var(--bg); }
  body { position: relative; font-family: "Arimo", Arial, sans-serif; color: var(--text); }

  .brand-mark { position: absolute; left: 48px; top: 0; width: 103px; height: 147px; background: #0d0d0d; }
  .brand-name { position: absolute; left: 177px; top: 61px; font-family: "Orbitron", sans-serif; font-weight: 500; font-size: 24px; color: var(--white); letter-spacing: 0.6px; white-space: nowrap; }

  .search { position: absolute; left: 925px; top: 14px; width: 161px; height: 20px; border-radius: 10px; background: linear-gradient(#9a9a9a, #6e6e6e); }
  .search svg { position: absolute; right: 2px; top: 1px; }
  .login { position: absolute; left: 1124px; top: 18px; font-size: 16px; color: var(--orange); text-decoration: none; }

  .rule { position: absolute; left: 0; width: 1200px; height: 1px; background: var(--rule); }
  .rule.top { top: 158px; }
  .rule.bottom { top: 236px; }

  .main-nav a { position: absolute; top: 191px; font-size: 16px; color: var(--text); text-decoration: none; white-space: nowrap; }

  .hero-art { position: absolute; left: 720px; top: 238px; width: 414px; height: 142px;
    background: linear-gradient(120deg, #000 0%, #2a2a2a 25%, #e8772a 50%, #f5f5f5 68%, #111 85%, #000 100%); }

  .page-title { position: absolute; left: 72px; top: 278px; font-size: 38px; font-weight: 700; color: var(--orange); }

  .form-row { position: absolute; left: 64px; width: 1070px; }
  .row-generics { top: 380px; height: 73px; background: var(--panel); }
  .row-medical { top: 453px; height: 73px; background: var(--panel-alt); }
  .row-mine { top: 526px; height: 371px; background: var(--panel); }
  .question { position: absolute; left: 32px; font-size: 19px; color: var(--text); white-space: nowrap; }
  .row-medical .question { font-weight: 700; color: var(--text-strong); left: 30px; }
  .opt { position: absolute; font-size: 18px; color: var(--text); white-space: nowrap; }
  .radio { position: absolute; width: 16px; height: 16px; border: 1.5px solid #cfcfcf; border-radius: 50%; }
  .radio.checked::after { content: ""; position: absolute; left: 4px; top: 4px; width: 5px; height: 5px; border-radius: 50%; background: #cfcfcf; }
  .check { position: absolute; left: 997px; width: 18px; height: 18px; border: 1.5px solid #cfcfcf; }

  .submit { position: absolute; left: 767px; top: 897px; width: 367px; height: 85px; background: var(--orange); color: var(--white); font-size: 24px; font-weight: 700; border: none; font-family: inherit; }

  .copyright { position: absolute; left: 0; width: 1095px; top: 1019px; text-align: center; font-size: 12px; color: var(--muted); }
</style>
</head>
<body>
  <header>
    <div class="brand-mark"></div>
    <div class="brand-name">Ironvale Shift Services</div>
    <div class="search">
      <svg width="18" height="18" viewBox="0 0 18 18"><circle cx="9" cy="9" r="8" fill="#111"/><circle cx="8" cy="8" r="3.5" fill="none" stroke="#fff" stroke-width="1.5"/><line x1="10.5" y1="10.5" x2="13.5" y2="13.5" stroke="#fff" stroke-width="1.5"/></svg>
    </div>
    <a class="login" href="#">LOGIN</a>
    <div class="rule top"></div>
    <nav class="main-nav">
      <a href="#" style="left:456px">HOME</a>
      <a href="#" style="left:551px">ABOUT</a>
      <a href="#" style="left:652px">DOWNLOAD DOCUMENTS</a>
      <a href="#" style="left:896px">PAY PORTAL</a>
      <a href="#" style="left:1043px">CONTACT US</a>
    </nav>
    <div class="rule bottom"></div>
  </header>

  <main>
    <div class="hero-art" role="img" aria-label="Illustrated mine rescue worker in orange and black"></div>
    <h1 class="page-title">APPLICATION FORM</h1>

    <section class="form-row row-generics">
      <p class="question" style="top:26px">DO YOU HAVE CURRENT COAL BOARD GENERICS ?</p>
      <span class="opt" style="left:777px;top:31px">YES</span><span class="radio checked" style="left:839px;top:33px"></span>
      <span class="opt" style="left:935px;top:31px">NO</span><span class="radio" style="left:989px;top:33px"></span>
    </section>

    <section class="form-row row-medical">
      <p class="question" style="top:25px">DO YOU HAVE A CURRENT &nbsp;COAL BOARD MEDICAL ?</p>
      <span class="opt" style="left:778px;top:25px">YES</span><span class="radio checked" style="left:840px;top:27px"></span>
      <span class="opt" style="left:936px;top:25px">NO</span><span class="radio" style="left:990px;top:27px"></span>
    </section>

    <section class="form-row row-mine">
      <p class="question" style="top:26px">WHAT MINE ARE YOU CURRENTLY INDUCTED AT ?</p>
      <span class="opt" style="left:774px;top:31px">TORVALECK</span><span class="check" style="top:30px"></span>
      <span class="opt" style="left:774px;top:89px">WENDARRIK</span><span class="check" style="top:87px"></span>
      <span class="opt" style="left:773px;top:154px">BRAXTONFELL</span><span class="check" style="top:152px"></span>
      <span class="opt" style="left:771px;top:212px">QUILLORANE</span><span class="check" style="top:210px"></span>
      <span class="opt" style="left:772px;top:271px">ETC.</span>
    </section>

    <button class="submit" type="submit">SUBMIT</button>
  </main>

  <footer class="copyright">Copyright : ISS. 2014</footer>
</body>
</html>
```